Branvique needs a business Card Design

We are looking for a business card Design for our new Managed Service Provider Company, Branvique. Branvique encompasses everything IT for the average medium sized business. Our primary services are help desk support, cyber-security (malware and ransomware protection), and Disaster Recovery systems. We would like the design to have a very clean and professional look, with a very minimalist feel.

Target Market(s)

Medium to large sized businesses

Industry/Entity Type

It Service

Contact Information for Business Card

Name GoesHere
name@branvique.com
O: 555-382-6047
C: 555-731-5820

Font styles to use
Other font styles liked:
• Poppins Font Only Please

Colors

Designer to choose only greyscale colors for use in the design.

Requirements
Must have
• Logo included
Nice to have
• Cutting Edge, innovative, minimalistic, elegant

```html
<!DOCTYPE html>
<html lang="en">
<head>
<meta charset="utf-8">
<title>Branvique Business Card</title>
<link href="https://fonts.googleapis.com/css2?family=Poppins:wght@300;400;500&display=swap" rel="stylesheet">
<style>
  :root {
    --bg: #dcdcdc;
    --card-white: #ffffff;
    --dark-top: #2e2e2e;
    --dark-bottom: #1a1a1a;
    --ink: #222222;
    --text-grey: #555555;
    --white: #ffffff;
  }
  * { margin: 0; padding: 0; box-sizing: border-box; }
  html, body {
    width: 1200px; height: 1200px; overflow: hidden;
    background: var(--bg);
    font-family: "Poppins", sans-serif;
  }
  .canvas { position: relative; width: 1200px; height: 1200px; }
  .card {
    position: absolute; left: 262px; width: 686px; height: 392px;
    border-radius: 22px; overflow: hidden;
  }
  .card-front { top: 165px; background: var(--card-white); }
  .card-back {
    top: 653px;
    background: linear-gradient(180deg, var(--dark-top) 0%, var(--dark-bottom) 100%);
  }
  .brand-square {
    position: absolute; left: 50%; width: 22px; height: 22px;
    transform: translateX(-50%);
  }
  .card-front .brand-square { top: 130px; background: var(--ink); }
  .card-back .brand-square { top: 170px; background: var(--white); }
  .front-brand {
    position: absolute; top: 168px; left: 0; right: 0; text-align: center;
    font-weight: 500; font-size: 30px; color: var(--ink); letter-spacing: 0.02em;
  }
  .holder-name {
    position: absolute; top: 280px; left: 0; right: 0; text-align: center;
    font-weight: 500; font-size: 21px; color: var(--ink); letter-spacing: 0.01em;
  }
  .contact-line {
    position: absolute; top: 315px; left: 0; right: 0;
    display: flex; justify-content: center; align-items: center; gap: 6px;
    font-weight: 400; font-size: 15.5px; color: var(--text-grey);
  }
  .contact-item { display: inline-flex; align-items: center; gap: 3px; }
  .contact-item svg { fill: var(--ink); }
  .website {
    position: absolute; top: 338px; left: 0; right: 0; text-align: center;
    font-weight: 400; font-size: 15px; color: var(--text-grey); letter-spacing: 0.22em;
  }
  .back-brand {
    position: absolute; top: 248px; left: 0; right: 0; text-align: center;
    font-weight: 300; font-size: 36px; color: var(--white);
    letter-spacing: 0.5em; padding-left: 0.5em;
  }
</style>
</head>
<body>
<div class="canvas">
  <section class="card card-front">
    <div class="brand-square"></div>
    <div class="front-brand">Branvique</div>
    <div class="holder-name">DANA WHITLOW</div>
    <div class="contact-line">
      <span class="contact-item">
        <svg width="13" height="13" viewBox="0 0 24 24" aria-hidden="true"><path d="M6.6 10.8a15.1 15.1 0 0 0 6.6 6.6l2.2-2.2c.3-.3.7-.4 1-.2 1.1.4 2.3.6 3.6.6.6 0 1 .4 1 1V20c0 .6-.4 1-1 1C10.6 21 3 13.4 3 4c0-.6.4-1 1-1h3.5c.6 0 1 .4 1 1 0 1.3.2 2.5.6 3.6.1.3 0 .7-.2 1z"/></svg>555-382-6047
      </span>
      <span class="contact-item">
        <svg width="11" height="15" viewBox="0 0 11 15" aria-hidden="true"><path d="M2 0h7a2 2 0 0 1 2 2v11a2 2 0 0 1-2 2H2a2 2 0 0 1-2-2V2a2 2 0 0 1 2-2zm0 2v10h7V2z"/></svg>&nbsp;555-731-5820
      </span>
      <span class="contact-item">
        <svg width="13" height="10" viewBox="0 0 13 10" aria-hidden="true"><path d="M0 0h13v10H0zM1.2 1.3v.4l5.3 3.6 5.3-3.6v-.4zm0 1.8v5.6h10.6V3.1L6.5 6.7z"/></svg>&nbsp;dana@branvique.com
      </span>
    </div>
    <div class="website">www.branvique.com</div>
  </section>

  <section class="card card-back">
    <div class="brand-square"></div>
    <div class="back-brand">BRANVIQUE</div>
  </section>
</div>
</body>
</html>
```